Design some Business Cards for Gleaming Wheel Studio

I require some business cards to be design for my car detailing business "Gleaming Wheel Studio".

Preferred layout is landscape and artwork MUST be created in CMYK format and 300 dpi. Information that should be included is

Marcus Whitby
Vehicle Detailing Specialist

Tel: 07715 492 618
Email : marcus@gleamingwheelstudio.co.uk
Website : www.gleamingwheelstudio.co.uk

One side should have just the logo and maybe some design element - I have attached a example of a business card which I do like the black side with the image just visible behind the text (example.jpg). The other side should have all of the contact information and probably the logo on it too.

Plenty of images on my website if needed www.gleamingwheelstudio.co.uk

It should have a classy look to it and be very simple and stylish .

Please do not use any templates or clip art

```html
<!DOCTYPE html>
<html lang="en">
<head>
<meta charset="utf-8">
<title>Gleaming Wheel Studio – Business Cards</title>
<link rel="stylesheet" href="https://fonts.googleapis.com/css2?family=PT+Sans:wght@400;700&display=swap">
<style>
  :root {
    --backdrop: #e9e7e3;
    --card-white: #ffffff;
    --card-grey: #e6e6e6;
    --card-black: #0b0b0b;
    --card-black-soft: #232323;
    --green: #8cc63f;
    --green-dark: #6fa52a;
    --ink: #2b2b2b;
    --ink-soft: #555555;
    --silver: #bdbdbd;
    --edge-dark: #3a3a3a;
  }
  * { box-sizing: border-box; margin: 0; padding: 0; }
  html, body {
    width: 1111px; height: 1200px; overflow: hidden;
    background: var(--backdrop);
    font-family: "PT Sans", Arial, sans-serif;
  }
  .sheet {
    width: 1111px; height: 1200px;
    display: flex; flex-direction: column; align-items: center; justify-content: center;
    gap: 70px;
  }
  .card {
    position: relative;
    width: 880px; height: 503px;
    border-radius: 4px;
    overflow: hidden;
    box-shadow: 0 10px 30px rgba(0,0,0,.18);
  }

  /* Front: contact side */
  .card--front {
    background: linear-gradient(160deg, var(--card-white) 0%, #f7f7f7 55%, var(--card-grey) 100%);
  }
  .card--front .edge-band {
    position: absolute; left: 0; right: 0; bottom: 0; height: 30px;
    background: var(--green);
    border-top: 3px solid var(--green-dark);
  }
  .card--front .edge-band::after {
    content: ""; position: absolute; left: 0; right: 0; bottom: 0; height: 8px;
    background: var(--edge-dark);
  }
  .brand {
    position: absolute; left: 70px; top: 78px;
    display: flex; align-items: center; gap: 16px;
  }
  .brand__mark {
    width: 46px; height: 46px; background: var(--silver);
  }
  .brand__name {
    font-size: 30px; font-weight: 400; letter-spacing: 3px; text-transform: uppercase;
    color: #8a8a8a;
  }
  .person {
    position: absolute; left: 70px; top: 300px;
  }
  .person__name {
    font-size: 44px; font-weight: 400; color: var(--green); line-height: 1.1;
  }
  .person__role {
    font-size: 25px; color: var(--ink); margin-top: 4px;
  }
  .divider {
    position: absolute; left: 470px; top: 262px; width: 2px; height: 150px;
    background: var(--green);
  }
  .contacts {
    position: absolute; left: 505px; top: 266px;
    list-style: none;
    display: flex; flex-direction: column; gap: 18px;
  }
  .contacts__item {
    display: flex; align-items: center; gap: 14px;
    font-size: 19px; color: var(--ink);
  }
  .contacts__icon {
    width: 28px; height: 28px; border-radius: 50%;
    background: var(--green);
    display: flex; align-items: center; justify-content: center;
    flex: none;
  }

  /* Back: logo side */
  .card--back {
    background:
      linear-gradient(125deg, rgba(255,255,255,.07) 0%, rgba(255,255,255,.02) 35%, rgba(255,255,255,0) 36%),
      radial-gradient(ellipse at 30% 40%, var(--card-black-soft) 0%, var(--card-black) 70%);
    display: flex; align-items: center; justify-content: center;
  }
  .card--back .brand-centre {
    display: flex; align-items: center; gap: 22px;
  }
  .card--back .brand__mark {
    width: 60px; height: 60px; background: var(--green);
  }
  .card--back .brand__name {
    font-size: 40px; letter-spacing: 4px; color: #e8e8e8;
  }
</style>
</head>
<body>
<main class="sheet">

  <section class="card card--front" aria-label="Business card, contact side">
    <div class="brand">
      <span class="brand__mark"></span>
      <span class="brand__name">Gleaming Wheel Studio</span>
    </div>

    <div class="person">
      <p class="person__name">Marcus Whitby</p>
      <p class="person__role">Vehicle Detailing Specialist</p>
    </div>

    <div class="divider"></div>

    <ul class="contacts">
      <li class="contacts__item">
        <span class="contacts__icon">
          <svg width="14" height="14" viewBox="0 0 24 24" aria-hidden="true"><path fill="#fff" d="M6.6 10.8a15.1 15.1 0 0 0 6.6 6.6l2.2-2.2c.3-.3.7-.4 1-.2 1.1.4 2.3.6 3.6.6.6 0 1 .4 1 1V20c0 .6-.4 1-1 1C10.6 21 3 13.4 3 4c0-.6.4-1 1-1h3.5c.6 0 1 .4 1 1 0 1.3.2 2.5.6 3.6.1.3 0 .7-.2 1z"/></svg>
        </span>
        07715 492 618
      </li>
      <li class="contacts__item">
        <span class="contacts__icon">
          <svg width="14" height="14" viewBox="0 0 24 24" aria-hidden="true"><path fill="#fff" d="M3 5h18v14H3z"/><path fill="none" stroke="#8cc63f" stroke-width="2" d="M3 6l9 7 9-7"/></svg>
        </span>
        marcus@gleamingwheelstudio.co.uk
      </li>
      <li class="contacts__item">
        <span class="contacts__icon">
          <svg width="14" height="14" viewBox="0 0 24 24" aria-hidden="true"><g fill="none" stroke="#fff" stroke-width="2"><circle cx="12" cy="12" r="9"/><path d="M3 12h18M12 3c3 3 3 15 0 18M12 3c-3 3-3 15 0 18"/></g></svg>
        </span>
        www.gleamingwheelstudio.co.uk
      </li>
    </ul>

    <div class="edge-band"></div>
  </section>

  <section class="card card--back" aria-label="Business card, logo side">
    <div class="brand-centre">
      <span class="brand__mark"></span>
      <span class="brand__name">Gleaming Wheel Studio</span>
    </div>
  </section>

</main>
</body>
</html>
```